we need a design for Water Bottle Lable Wrap
The product is called Corvane Water is a restructured water. its a very healthy and rejuvenating water
we were looking at using as a tag ling Restore, Recover, Rejuvenate.

```html
<!DOCTYPE html>
<html lang="en">
<head>
<meta charset="UTF-8">
<title>Corvane Water – Bottle Label Wrap</title>
<link rel="stylesheet" href="https://fonts.googleapis.com/css2?family=Poppins:wght@400;600;800&display=swap">
<style>
  :root {
    --stage-grey: #d6d6d6;
    --label-white: #ffffff;
    --wave-pale: #d9effb;
    --wave-light: #8fcbf0;
    --wave-mid: #5aa6e2;
    --wave-deep: #3a7fca;
    --brand-blue: #1466b3;
    --text-white: #ffffff;
  }
  * { margin: 0; padding: 0; box-sizing: border-box; }
  html, body {
    width: 1005px;
    height: 1200px;
    overflow: hidden;
    background: var(--stage-grey);
    font-family: "Poppins", sans-serif;
  }
  .canvas {
    width: 1005px;
    height: 1200px;
    display: flex;
    align-items: center;
    justify-content: center;
  }
  .label-wrap {
    position: relative;
    width: 880px;
    height: 220px;
    overflow: hidden;
    box-shadow: 0 2px 4px rgba(0, 0, 0, 0.18);
  }
  .label-waves {
    position: absolute;
    inset: 0;
    background:
      radial-gradient(ellipse 70% 80% at 50% 0%, var(--label-white) 0%, var(--label-white) 35%, var(--wave-pale) 55%, rgba(217, 239, 251, 0) 80%),
      linear-gradient(180deg, var(--wave-pale) 0%, var(--wave-light) 40%, var(--wave-mid) 72%, var(--wave-deep) 100%);
  }
  .label-content {
    position: relative;
    height: 100%;
    display: flex;
    flex-direction: column;
    align-items: center;
    padding-top: 34px;
    text-align: center;
  }
  .brand-name {
    font-weight: 600;
    font-size: 58px;
    line-height: 1;
    color: var(--brand-blue);
    letter-spacing: 0.5px;
  }
  .product-type {
    margin-top: 16px;
    font-weight: 800;
    font-size: 42px;
    line-height: 1;
    color: var(--text-white);
    letter-spacing: 1px;
  }
  .tagline {
    margin-top: 14px;
    font-weight: 400;
    font-size: 14px;
    color: var(--text-white);
    letter-spacing: 0.3px;
  }
</style>
</head>
<body>
  <main class="canvas">
    <section class="label-wrap" aria-label="Corvane Water bottle label wrap">
      <div class="label-waves" role="img" aria-label="Soft layered blue water waves fading to white at the top"></div>
      <div class="label-content">
        <h1 class="brand-name">Corvane</h1>
        <p class="product-type">WATER</p>
        <p class="tagline">Restore, Recover, Rejuvenate</p>
      </div>
    </section>
  </main>
</body>
</html>
```